Water ATM Card

Need a design for water ATM cards. Size of card is 3.375 x 2.125 inch
On the Front include the Cedar Brook Logo.
Bottom right corner should have Price $100
On the Back
This card is to be used to access water refills at any Cedar Brook Water Vending Machines.
Please contact (869) 415 2983 or (869) 238 4617 or email clearflowhub@mailbox-example.com for any assistance or recharging of card.

```html
<!DOCTYPE html>
<html lang="en">
<head>
<meta charset="utf-8">
<title>Cedar Brook Water ATM Card</title>
<link rel="stylesheet" href="https://fonts.googleapis.com/css2?family=Bebas+Neue&family=Montserrat:wght@600;700;800&display=swap">
<style>
  :root {
    --page-bg: #2e2f31;
    --card-white: #ffffff;
    --brand-blue: #1577c2;
    --deep-blue: #1a5fae;
    --brand-green: #4aa843;
    --navy-edge: #262a6b;
    --ink: #111111;
    --water-light: #dff1fb;
    --water-mid: #8fd0f0;
    --water-deep: #3ea3dc;
  }
  * { box-sizing: border-box; margin: 0; padding: 0; }
  html, body { width: 1200px; height: 904px; overflow: hidden; }
  body { background: var(--page-bg); position: relative; font-family: "Montserrat", sans-serif; }

  .card {
    position: absolute;
    width: 620px;
    height: 390px;
    background: var(--card-white);
    overflow: hidden;
    box-shadow: 0 14px 30px rgba(0,0,0,.45);
  }
  .card--back { left: 110px; top: 46px; }
  .card--front { left: 470px; top: 466px; border-bottom: 7px solid var(--navy-edge); }

  /* brand lockup */
  .brand { display: flex; align-items: center; justify-content: center; gap: 12px; }
  .brand__dot { width: 34px; height: 34px; border-radius: 50%; background: var(--brand-green); }
  .brand__name { font-weight: 800; color: var(--deep-blue); font-size: 40px; letter-spacing: 1px; text-transform: uppercase; white-space: nowrap; }

  /* back */
  .back__notice {
    font-family: "Bebas Neue", sans-serif;
    color: var(--ink);
    font-size: 37px;
    line-height: 1.02;
    padding: 26px 30px 0;
  }
  .back__brand { margin-top: 26px; }
  .back__band {
    position: absolute; left: 0; right: 0; bottom: 0; height: 170px;
    background: var(--brand-blue);
    color: var(--card-white);
    display: flex; align-items: center; justify-content: center;
    text-align: center;
    font-weight: 600; font-size: 21px; line-height: 1.45;
    padding: 0 20px;
  }

  /* front */
  .front__pill {
    position: absolute; left: 34px; top: 30px;
    padding: 8px 24px;
    border-radius: 30px;
    background: var(--brand-blue);
    border: 3px solid var(--brand-green);
    color: var(--card-white);
    font-weight: 700; font-size: 21px; letter-spacing: .5px;
    white-space: nowrap;
  }
  .front__water {
    position: absolute; left: 0; right: 0; bottom: 0; height: 190px;
    background: linear-gradient(170deg, var(--card-white) 0%, var(--water-light) 35%, var(--water-mid) 70%, var(--water-deep) 100%);
  }
  .front__brand { position: absolute; left: 0; right: 0; top: 130px; }
  .front__price {
    position: absolute; right: 34px; bottom: 90px;
    font-weight: 800; font-size: 30px; color: var(--ink);
  }
</style>
</head>
<body>

  <section class="card card--back" aria-label="Card back">
    <p class="back__notice">This card is to be used to access water refills<br>at any Cedar Brook water vending machines.</p>
    <div class="brand back__brand">
      <span class="brand__dot"></span>
      <span class="brand__name">Cedar Brook</span>
    </div>
    <div class="back__band">
      <p>Contact (869) 415 2983 or (869) 238 4617<br>or email clearflowhub@mailbox-example.com<br>for any assistance or recharging of card.</p>
    </div>
  </section>

  <section class="card card--front" aria-label="Card front">
    <div class="front__water" role="img" aria-label="Splash of clear blue water with bubbles"></div>
    <div class="front__pill">CEDAR BROOK WATER ATM CARD</div>
    <div class="brand front__brand">
      <span class="brand__dot"></span>
      <span class="brand__name">Cedar Brook</span>
    </div>
    <p class="front__price">Price $100</p>
  </section>

</body>
</html>
```